One Page Advertisement in Tradeshow Brochure

** URGENT DEADLINE - 24 hours **
We are a vendor at a Manufacturing Tradeshow. We are selling Cybersecurity & IT Services to new potential clients in the Manufacturing industry . We need a one page 8x11 layout for the program booklet that will be passed out to attendees at the tradeshow.

We have a basic draft we designed inhouse that needs to be redesigned to look more professional and polished. Please use the information we have on our design as it's all needed to be on the ad. Our ad needs to showcase we are EXPERTS in providing CYBERSECURITY to the Manufacturing Industry. Manufacturing is our top vertical market we service. We also provide IT support as well. Another important detail is to make sure we tell people to visit booth #400 to sign up for a free cybersecurity assessment. The popup bubble is an option. If you can make it work, thats ok AND IF NOT, thats ok too. The message is relevant to what we are educating people on, but whether you can make it look good or not, is an option.

We like the idea of a hacker image. It immediately catches attention and tells people what we are about and what we do.... without talking to us first. I would love a side image of a hacker - if that were possible so that we could use this similar full page ad on a tall skinny pop up banner at our trade show booth. We are purchasing a tall pop up banner for our booth that needs to mimic the full page ad. This will help people identify us at our tradeshow booth because the ad and banner will be designed similar (Same look and feel). The tall pop up banner will be project #2 for you. We can work on that project as soon as the ad is done. I share this #2 project with you so that you know we need another item designed that needs to mirror the booklet advertisement.

This project is VERY URGENT with a 24 hour deadline!! I need this done within 24 hours. I will be readily available to assist with any questions or input throughout the next 24 hours. I have to turn in this ad artwork tomorrow end of day.

We like the idea of a hacker as a main picture/background for the ad. In addition to this full page ad, we will want to take this same info from the 8x11 ad and make a tall pop up banner for our trade show booth. So, there's more project work needed from you (but we have a few extra days before the tall popup banner is required/deadline). The ad is due now and most important. Just be sure to design the ad with the tall popup banner in mind. :) We want them to look very similar.

Thank you!

Target Market(s)

Businesses who need cybersecurity services - our vertical market is manufacturing

Industry/Entity Type

Cybersecurity / Technology / IT Services

Font styles to use
Sans Serif

Colors
0054AA
0677BA
7BADD7
CADEEF
E8F1F8
0094D4
00A9DD
6FCCEA
C7EBF8
E9F6FB
FFF300
FFF600
FEFA6F
FFFEC7
FFFEE8
FFC000
F8CF3A
FAE287
FDF2CF
FEFAEE
EB3D1F
EC4F4E
F09395
F8D3D4
FCEDEE

Requirements
Must have
• all the content on the sample image we provided - with the ex ception of the hacker image and background. Those can be redesigned. Its the wording that has to be included in the design. Feel free to move the wording around and redesign.
Nice to have
• Modern & Clean Fonts - colorful - stand out - techy - cybersecurity - hacker image (you can use a different hacker if you prefer)
Should not have
• No serif type fonts - they are too old and traditional. Don't make the overall design too busy/cluttered

```html
<!DOCTYPE html>
<html lang="en">
<head>
<meta charset="utf-8">
<title>Citadel Systems – Tradeshow Advertisement</title>
<link rel="stylesheet" href="https://fonts.googleapis.com/css2?family=Source+Sans+3:ital,wght@0,400;0,600;0,700;0,800;1,600;1,700&display=swap">
<style>
  :root {
    --navy-deep: #050d1f;
    --navy: #0a1a3a;
    --blue: #0054aa;
    --blue-bright: #0094d4;
    --cyan: #00a9dd;
    --yellow: #fff300;
    --yellow-soft: #fffec7;
    --gold: #f8cf3a;
    --gold-dark: #b8860b;
    --white: #ffffff;
    --booth-dark: #1c2f4e;
    --font-main: "Source Sans 3", Arial, sans-serif;
  }
  * { margin: 0; padding: 0; box-sizing: border-box; }
  html, body { width: 929px; height: 1200px; overflow: hidden; background: var(--navy-deep); }
  .ad {
    position: relative;
    width: 929px;
    height: 1200px;
    overflow: hidden;
    font-family: var(--font-main);
    color: var(--white);
    background: var(--navy-deep);
  }
  .hero-photo {
    position: absolute;
    left: 0; top: 0;
    width: 929px; height: 990px;
    background:
      radial-gradient(ellipse at 72% 45%, rgba(40,110,170,0.55) 0%, rgba(10,30,60,0) 55%),
      radial-gradient(ellipse at 45% 85%, rgba(0,148,212,0.35) 0%, rgba(5,13,31,0) 50%),
      linear-gradient(160deg, #0d2038 0%, #0a1a30 40%, #07142a 70%, #040a18 100%);
  }
  .headline {
    position: absolute;
    left: 66px; top: 52px;
    font-weight: 700;
    font-size: 47px;
    line-height: 52px;
    letter-spacing: -0.5px;
  }
  .headline p + p { margin-top: 20px; }
  .headline em { color: var(--yellow); font-style: italic; }
  .headline .ready { color: var(--yellow); margin-top: 22px; font-size: 50px; }
  .award-badge {
    position: absolute;
    left: 711px; top: 10px;
    width: 190px; height: 190px;
  }
  .services {
    position: absolute;
    left: 66px; top: 472px;
  }
  .services-title {
    color: var(--yellow);
    font-style: italic;
    font-weight: 600;
    font-size: 24px;
    margin-bottom: 8px;
  }
  .services-list { list-style: none; }
  .services-list li {
    font-size: 32px;
    font-weight: 600;
    line-height: 43px;
    padding-left: 22px;
    position: relative;
  }
  .services-list li::before {
    content: "";
    position: absolute;
    left: 0; top: 20px;
    width: 8px; height: 8px;
    border-radius: 50%;
    background: var(--white);
  }
  .tagline {
    position: absolute;
    left: 90px; top: 820px;
    color: var(--yellow);
    font-weight: 700;
    font-size: 33px;
    line-height: 43px;
  }
  .booth {
    position: absolute;
    right: 0; top: 658px;
    width: 180px;
  }
  .booth-shape { position: absolute; left: 0; top: 0; }
  .booth-text {
    position: absolute;
    right: 14px;
    text-align: right;
  }
  .booth-visit { top: 8px; font-size: 18px; color: var(--navy); font-weight: 600; }
  .booth-number { top: 40px; font-size: 50px; font-weight: 800; color: var(--white); line-height: 60px; }
  .booth-offer { top: 114px; color: var(--navy); line-height: 1.1; }
  .booth-offer .small { font-size: 16px; font-weight: 600; }
  .booth-offer .free { font-size: 34px; font-weight: 800; vertical-align: -3px; }
  .booth-offer .line { font-size: 15px; font-weight: 600; display: block; }
  .divider {
    position: absolute;
    left: 0; top: 986px;
    width: 929px; height: 5px;
    background: var(--yellow);
  }
  .footer-band {
    position: absolute;
    left: 0; top: 991px;
    width: 929px; height: 209px;
    background:
      radial-gradient(ellipse at 15% 40%, rgba(0,148,212,0.35) 0%, rgba(5,13,31,0) 45%),
      linear-gradient(180deg, #0a1a3a 0%, #081530 100%);
  }
  .brand {
    position: absolute;
    left: 655px; top: 1050px;
    display: flex;
    align-items: center;
    gap: 12px;
  }
  .brand-dot {
    width: 50px; height: 50px;
    border-radius: 50%;
    background: var(--white);
  }
  .brand-name {
    font-size: 36px;
    font-weight: 700;
    color: var(--white);
    line-height: 1;
  }
  .contact {
    position: absolute;
    right: 24px; top: 1133px;
    text-align: right;
    font-size: 15px;
    line-height: 24px;
    color: var(--white);
  }
</style>
</head>
<body>
<main class="ad">
  <div class="hero-photo" role="img" aria-label="Hooded hacker typing on a laptop in a dark room, lit by blue screens and glowing circuit board lights"></div>

  <header class="headline">
    <p>It’s not a matter<br>of will you get hacked.</p>
    <p>It’s a matter of <em>when</em><br>you get hacked.</p>
    <p class="ready">Are you ready?</p>
  </header>

  <svg class="award-badge" viewBox="0 0 190 190" aria-hidden="true">
    <defs>
      <radialGradient id="badgeGold" cx="40%" cy="35%" r="70%">
        <stop offset="0%" stop-color="#fae287"/>
        <stop offset="55%" stop-color="#d9a520"/>
        <stop offset="100%" stop-color="#8a5e08"/>
      </radialGradient>
    </defs>
    <circle cx="95" cy="95" r="92" fill="url(#badgeGold)"/>
    <circle cx="95" cy="95" r="72" fill="#1a1208"/>
  </svg>

  <section class="services">
    <p class="services-title">IT Services Providing:</p>
    <ul class="services-list">
      <li>Managed Cybersecurity</li>
      <li>Fully Managed IT</li>
      <li>Co-Managed IT</li>
      <li>Cloud Services</li>
      <li>Business Continuity</li>
      <li>IT Projects</li>
      <li>Phone Service</li>
    </ul>
  </section>

  <p class="tagline">Delivering managed<br>IT Cybersecurity Services<br>to the Manufacturing Industry.</p>

  <aside class="booth">
    <svg class="booth-shape" width="180" height="206" viewBox="0 0 180 206" aria-hidden="true">
      <polygon points="18,0 180,0 180,36 4,36" fill="var(--yellow)"/>
      <polygon points="4,36 180,36 180,112 0,112" fill="var(--booth-dark)"/>
      <polygon points="0,112 180,112 180,206 18,206" fill="var(--yellow)"/>
    </svg>
    <div class="booth-text booth-visit">Visit Booth</div>
    <div class="booth-text booth-number">#400</div>
    <div class="booth-text booth-offer">
      <span class="small">Sign up for a </span><span class="free">FREE</span>
      <span class="line">Cybersecurity Assessment</span>
      <span class="line">($2500 Value)</span>
    </div>
  </aside>

  <div class="divider"></div>
  <footer class="footer-band" role="img" aria-label="Dark blue band with faint glowing circuit board traces"></footer>

  <div class="brand">
    <span class="brand-dot"></span>
    <span class="brand-name">Citadel Systems</span>
  </div>

  <address class="contact" style="font-style:normal">
    4520 Ridgeline Pkwy., Austin, TX 78731<br>
    (512) 555-0148 (CSIT) • help@citadelsys.com • citadelsys.com
  </address>
</main>
</body>
</html>
```